Startup High Tech Software Company Needs a Web Design (4 pages)

We need a web design for a startup high tech software company based in Brazil called Zumvi. We are known to build extremely fast softwares with high qualities for web and mobile (Android and iOS) applications.
We still don't have all the content to build the institutional web site, but we'd like to have the design already so we can change the content on demand later.
Basically we're requesting a home page and 3 templates of internal pages with spaces to videos and images.
Below are some examples of sites (please ignore the style, this is just to show the distribution of the main content):
Home: http://www.plorvet.com.br/
Internal pages: http://www.quendal.com/brightsphere/us/en/embedded_systems/industries/index.html
http://www-01.quendal.com/software/lumetra/solutions/automotive/
http://www.quendal.com/brightsphere/us/en/embedded_systems/overview/index.html?lnk=ushpls1

The header and footer of Quendal's web site's positions looks good for us (not the same style).

The first impression should be representing exactly what we are, fast and innovative company with high quality professionals.

Please consider the logos attached. We'd like to have a web site that combines with these logos. You can use either one (horizontal or vertical) depending on the place it is located.

Target Market(s)

CIO, IT managers of mid to big size companies

Industry/Entity Type

Automotive

Requirements
Must have
• HTML, CSS (responsive CSS is preferred) and images like buttons with no text inside, because the web site is going to have different languages so we can edit them easily.
Like Quendal, some link or combobox to change the language.
Nice to have
• Timer to change the main content of the home page (not flash).
Should not have
• Flash

```html
<!DOCTYPE html>
<html lang="en">
<head>
<meta charset="utf-8">
<title>Zumvi — Extremely Fast Software</title>
<link rel="stylesheet" href="https://fonts.googleapis.com/css2?family=Arimo:ital,wght@0,400;0,700;1,400&family=Gentium+Book+Plus:wght@400;700&display=swap">
<style>
  :root {
    --bar-dark: #333333;
    --nav-text: #cfcfcf;
    --phone-blue: #8cc8f2;
    --brand-navy: #163a5c;
    --button-blue: #00649a;
    --heading-grey: #565656;
    --sub-grey: #8a8a8a;
    --accent-blue: #1a6ea0;
    --band-blue: #7fb1e3;
    --crm: #3a36c9;
    --web: #ff9933;
    --ios: #ff3333;
    --android: #3399cc;
    --footer-dark: #3b3b3b;
    --footer-text: #e4e4e4;
    --white: #ffffff;
  }
  * { margin: 0; padding: 0; box-sizing: border-box; }
  html, body { width: 1200px; height: 1000px; overflow: hidden; background: var(--white); }
  body { position: relative; font-family: "Arimo", Arial, sans-serif; }
  .abs { position: absolute; }

  .top-bar { left: 0; top: 0; width: 1200px; height: 64px; background: var(--bar-dark); }
  .nav-link { top: 21px; font-size: 18px; color: var(--nav-text); letter-spacing: .2px; }
  .phone-icon { left: 997px; top: 16px; width: 34px; height: 34px; }
  .phone-number { left: 1043px; top: 32px; font-size: 14px; font-weight: 700; color: var(--phone-blue); }

  .logo-box { left: 0; top: 24px; width: 272px; height: 118px; background: var(--white);
    border-right: 3px solid #2a2a2a; border-bottom: 3px solid #2a2a2a;
    display: flex; align-items: center; padding-left: 8px; gap: 12px; }
  .logo-square { width: 50px; height: 50px; background: var(--brand-navy); }
  .logo-name { font-size: 52px; font-weight: 700; color: var(--brand-navy); }

  .hero { left: 0; top: 64px; width: 1200px; height: 360px;
    background: radial-gradient(ellipse at 50% 50%, #bdbdbd 0%, #9c9c9c 55%, #7c7c7c 100%); }
  .hero-kicker { left: 0; width: 1200px; top: 198px; text-align: center; font-style: italic; font-size: 16px; color: #f2f2f2; }
  .hero-title { left: 0; width: 1200px; top: 226px; text-align: center; font-size: 58px; font-weight: 700;
    color: var(--white); letter-spacing: 1.5px; }
  .hero-rule { left: 140px; top: 269px; width: 920px; height: 1px; background: rgba(255,255,255,.8); }
  .contact-button { left: 489px; top: 341px; width: 222px; height: 64px; background: var(--button-blue);
    border-radius: 8px; box-shadow: 0 3px 4px rgba(0,0,0,.55); color: var(--white); font-size: 30px;
    display: flex; align-items: center; justify-content: center; letter-spacing: .5px; }

  .intro-heading { left: 0; width: 1200px; top: 432px; text-align: center; font-size: 36px; font-weight: 700; color: var(--heading-grey); }
  .intro-line { top: 452px; height: 3px; background: #8a8a8a; border-bottom: 1px solid #d0d0d0; }
  .intro-sub { left: 0; width: 1200px; top: 479px; text-align: center; font-family: "Gentium Book Plus", Georgia, serif;
    font-size: 19px; color: var(--sub-grey); letter-spacing: .3px; }
  .intro-sub .accent { color: var(--accent-blue); }

  .services { left: 0; top: 519px; width: 1200px; height: 295px; background: var(--band-blue); }
  .service-dot { top: 543px; width: 105px; height: 105px; border-radius: 50%; border: 1px solid #e6f0fa;
    display: flex; align-items: center; justify-content: center; font-family: "Gentium Book Plus", Georgia, serif;
    font-size: 22px; color: var(--white); text-shadow: 1px 1px 0 rgba(0,0,0,.55), -1px -1px 0 rgba(0,0,0,.25); }
  .service-dot.crm { left: 123px; background: var(--crm); color: #c9c9e8; }
  .service-dot.web { left: 409px; background: var(--web); color: #a5400a; }
  .service-dot.ios { left: 697px; background: var(--ios); color: #9c0d0d; }
  .service-dot.android { left: 984px; background: var(--android); color: #17365a; font-size: 18px; }
  .service-stem { top: 648px; width: 4px; height: 45px; background: var(--white); }
  .service-frame { left: 49px; top: 692px; width: 1102px; height: 81px; border: 2px solid var(--white); border-radius: 10px; }
  .service-text { top: 706px; width: 150px; font-family: "Gentium Book Plus", Georgia, serif; font-size: 14px;
    line-height: 14px; color: var(--white); }

  .footer { left: 0; top: 857px; width: 1200px; height: 143px;
    background: linear-gradient(#474747, var(--footer-dark) 40%, #333); }
  .footer-title { left: 80px; top: 870px; font-family: "Gentium Book Plus", Georgia, serif; font-size: 24px; color: var(--footer-text); letter-spacing: 1px; }
  .footer-item { left: 80px; font-family: "Gentium Book Plus", Georgia, serif; font-size: 19px; color: var(--footer-text);
    letter-spacing: .8px; display: flex; align-items: center; gap: 8px; }
  .bullet { width: 12px; height: 12px; }
  .footer-link { font-family: "Gentium Book Plus", Georgia, serif; font-size: 19px; color: var(--footer-text); letter-spacing: 1px; }
  .social-square { top: 934px; width: 29px; height: 29px; border-radius: 4px;
    background: linear-gradient(#f4f4f4, #a9a9a9); }
</style>
</head>
<body>
  <header>
    <div class="abs top-bar"></div>
    <nav>
      <span class="abs nav-link" style="left:292px">ABOUT US</span>
      <span class="abs nav-link" style="left:468px">PRODUCTS</span>
      <span class="abs nav-link" style="left:673px">for WEB</span>
      <span class="abs nav-link" style="left:833px">for MOBILE</span>
    </nav>
    <svg class="abs phone-icon" viewBox="0 0 34 34" aria-hidden="true">
      <rect width="34" height="34" rx="6" fill="#8cc8f2"/>
      <path d="M11 7 h4 l2 6 -3 2 q2 5 6 7 l2 -3 6 2 v4 q-1 3 -4 3 q-10 -1 -15 -14 q0 -4 2 -7z" fill="#1d2d3c"/>
    </svg>
    <span class="abs phone-number">0040 555 018274</span>
    <div class="abs logo-box"><span class="logo-square"></span><span class="logo-name">ZUMVI</span></div>
  </header>

  <main>
    <section>
      <div class="abs hero" role="img" aria-label="Photo of a chalkboard covered with handwritten mathematical formulas"></div>
      <p class="abs hero-kicker">if you are looking for</p>
      <h1 class="abs hero-title">EXTREMLY FAST SOFTWARE</h1>
      <div class="abs hero-rule"></div>
      <div class="abs contact-button">contact us</div>
    </section>

    <section>
      <div class="abs intro-line" style="left:200px;width:258px"></div>
      <div class="abs intro-line" style="left:744px;width:256px"></div>
      <h2 class="abs intro-heading">We are ZUMVI</h2>
      <p class="abs intro-sub">There are many variations of passages of Lorem <span class="accent">Ipsum</span> available</p>
    </section>

    <section>
      <div class="abs services"></div>
      <div class="abs service-dot crm">CRM</div>
      <div class="abs service-dot web">WEB</div>
      <div class="abs service-dot ios">IOS</div>
      <div class="abs service-dot android">ANDROID</div>
      <div class="abs service-stem" style="left:173px"></div>
      <div class="abs service-stem" style="left:459px"></div>
      <div class="abs service-stem" style="left:747px"></div>
      <div class="abs service-stem" style="left:1034px"></div>
      <div class="abs service-frame"></div>
      <p class="abs service-text" style="left:115px">Proin ut nibh luctus, porta ligula ut, tempor lacus. Duis arcu mauris,</p>
      <p class="abs service-text" style="left:404px">Proin ut nibh luctus, porta ligula ut, tempor lacus. Duis arcu mauris,</p>
      <p class="abs service-text" style="left:689px">Proin ut nibh luctus, porta ligula ut, tempor lacus. Duis arcu mauris,</p>
      <p class="abs service-text" style="left:979px">Proin ut nibh luctus, porta ligula ut, tempor lacus. Duis arcu mauris,</p>
    </section>
  </main>

  <footer>
    <div class="abs footer"></div>
    <h3 class="abs footer-title">PRODUCTS</h3>
    <div class="abs footer-item" style="top:908px">
      <svg class="bullet" viewBox="0 0 12 12" aria-hidden="true"><circle cx="6" cy="6" r="5" fill="none" stroke="#ddd" stroke-width="1.4"/><path d="M5 3.5 L8 6 L5 8.5z" fill="#ddd"/></svg>
      <span>web development</span>
    </div>
    <div class="abs footer-item" style="top:947px">
      <svg class="bullet" viewBox="0 0 12 12" aria-hidden="true"><circle cx="6" cy="6" r="5" fill="none" stroke="#ddd" stroke-width="1.4"/><path d="M5 3.5 L8 6 L5 8.5z" fill="#ddd"/></svg>
      <span>mobile IOS, Android</span>
    </div>
    <svg class="abs" style="left:800px;top:882px" width="35" height="24" viewBox="0 0 35 24" aria-hidden="true">
      <rect x="1" y="1" width="33" height="22" fill="none" stroke="#5a9ad6" stroke-width="1.6"/>
      <path d="M1 1 L17.5 14 L34 1 M1 23 L13 11 M34 23 L22 11" fill="none" stroke="#5a9ad6" stroke-width="1.6"/>
    </svg>
    <span class="abs footer-link" style="left:851px;top:882px">get in touch</span>
    <div class="abs social-square" style="left:801px"></div>
    <div class="abs social-square" style="left:858px"></div>
    <div class="abs social-square" style="left:915px"></div>
    <span class="abs footer-link" style="left:971px;top:944px">follow us</span>
  </footer>
</body>
</html>
```